Redesign of tourdepays.com website (3 page types)

We need a fresh rebrush of www.tourdepays.com, a portal for french regions, departements and cities. It shall look modern as the current design is over 10 years old.

We like the blueish colors and the french touch (blue, white, red).

There are 3 page types that we currently need:
- Homepage (http://www.tourdepays.com/)
- Region overview (e.g. http://www.tourdepays.com/provence-alpes-cote-d-azur)
- City overview (e.g. http://www.tourdepays.com/provence-alpes-cote-d-azur/bouches-du-rhone/marseille)

See "Must have" for a more detailed briefing. All required elements exist and need a rebrush/redesign

Requirements
Must have
• General:

- 3 column layout
+ Header
+ Left sidebar
+ Content area
+ Right sidebar (250px inner width for ads)
+ Footer
- 3 classes of headlines
- Simple sidebar widgets (headline & content / without headline)

Header:
- Logo
- 2 or 3 links
- Search box
- Breadcrumb navigation

Footer:
- Nothing special, really

Homepage:
- Nice looking map with visible region borders to create a mouseover effect (as seen on current version). Meaning we need the plain map and a version with each region highlighted
- Text areas
- Content boxes (like the current gray ones)

Region overview
- Headline
- Info box (Informations)
- Mini map
- Crest / emblem
- Text area with headline for a long descriptive text with a "read more" / "show less" button/link to pop out the whole text via javascript
- List of the 24 biggest cities in the region

City overview
- Headline
- Info box (Informations, same look as for regions)
- Mini map
- List of the 24 cities nearby
- List of available photos
- Example sidebar widgets (right sidebar):
+ Upload a photo of this city
+ Weather conditions
+ Link list
Nice to have
• - A new favicon
- Friendbook og:image
Should not have
• - Flash
- Animations

```html
<!DOCTYPE html>
<html lang="fr">
<head>
<meta charset="utf-8">
<title>tourdepays.com – Les villes de France</title>
<link rel="stylesheet" href="https://fonts.googleapis.com/css2?family=Arimo:wght@400;700&display=swap">
<style>
  :root{
    --blue:#1a4fb0;
    --blue-dark:#143f93;
    --blue-link:#1f4aa8;
    --red:#c8141b;
    --red-line:#d23a3a;
    --text:#666;
    --text-dark:#222;
    --grey-box:#e0e0e0;
    --dots:#b5b5b5;
    --footer:#3a3a3a;
  }
  *{box-sizing:border-box;margin:0;padding:0}
  html,body{width:680px;height:1200px;overflow:hidden;background:#fff}
  body{position:relative;font-family:"Arimo",Arial,sans-serif;color:var(--text)}
  a{color:inherit;text-decoration:none}

  /* Header */
  .site-header{position:absolute;left:0;top:0;width:680px;height:38px;background:linear-gradient(#2457bd,var(--blue-dark))}
  .brand{position:absolute;left:80px;top:9px;color:#fff;font-size:17px;font-weight:700;letter-spacing:.2px}
  .main-nav{position:absolute;left:281px;top:16px;font-size:8px;color:#fff;display:flex}
  .main-nav a{padding:0 6px}
  .main-nav a:first-child{padding-left:0}
  .main-nav span{color:#cfd9f0}
  .search{position:absolute;left:499px;top:13px;width:101px;height:14px;background:#fff;border:1px solid #c9c9c9}
  .search svg{position:absolute;right:3px;top:1px}

  /* Hero */
  .hero{position:absolute;left:0;top:38px;width:680px;height:206px;
    background:linear-gradient(180deg,#3d86d6 0%,#7db8e8 22%,#8d9a6a 45%,#4d7a3a 62%,#3c6f86 78%,#2d5a6a 100%)}
  .hero-arrow{position:absolute;top:71px}
  .hero-arrow.prev{left:28px}
  .hero-arrow.next{left:638px}
  .caption{position:absolute;color:#fff;font-size:11.5px;padding:2px 5px;white-space:nowrap}
  .caption.primary{left:105px;top:127px;background:var(--red)}
  .caption.secondary{left:150px;top:146px;background:var(--blue-dark)}

  /* Columns */
  .col{position:absolute;top:266px}
  .col-left{left:80px;width:96px}
  .col-main{left:196px;width:251px}
  .col-right{left:467px;width:134px}

  .widget-title{font-size:12px;color:var(--text-dark);padding-bottom:4px;border-bottom:1.5px solid var(--red-line);font-weight:400}
  .link-list{list-style:none;font-size:7.7px;color:#444;margin-top:2px}
  .link-list li{height:16px;line-height:16px;white-space:nowrap}
  .col-right .link-list li{padding-left:9px}

  .section-title{font-size:12px;color:var(--text-dark);font-weight:400}
  .lead{font-size:8.2px;color:#333;margin:5px 0 0 2px}
  .map{position:absolute;left:12px;top:36px;width:221px;height:240px;
    background:radial-gradient(ellipse at 50% 45%,#5fb7a8 0%,#8a7fc8 35%,#e06a8c 60%,#f0c040 80%,rgba(255,255,255,0) 100%);
    border-radius:42% 48% 40% 44%}
  .copy{font-size:7.3px;line-height:9.7px;text-align:justify;color:var(--text)}
  .copy p+p{margin-top:9.7px}
  .copy .city{color:var(--blue-link)}
  .divider{border:0;border-top:1px dotted var(--dots)}

  .thumb{float:left;width:69px;height:56px;margin:0 7px 3px 1px;border:1px solid #ddd;padding:3px;background:#fff}
  .thumb span{display:block;width:100%;height:100%}
  .thumb .sea{background:linear-gradient(#bcd3e4 0%,#8faabb 45%,#5a7d8c 70%,#6e8c6a 100%)}
  .thumb.news{height:46px}
  .thumb .portrait{background:linear-gradient(135deg,#5b4636,#a07a5c 55%,#4a3a2e)}
  .news-title{font-size:9px;color:var(--red);line-height:11px;font-weight:400}
  .more{display:block;text-align:right;font-size:8px;color:var(--blue-link)}

  .ad{width:134px;height:133px;background:var(--grey-box);display:flex;align-items:center;justify-content:center;font-size:15px;color:#111}
  .ad.promo{background:linear-gradient(160deg,#1d58b8 0%,#2a6fd0 40%,#f0a020 70%,#d8261c 100%)}

  /* Social box */
  .social{position:absolute;left:80px;top:705px;width:96px;height:144px;border:1px solid #c9c9c9;background:#fff;font-size:6px;color:#333}
  .social-head{display:flex;gap:4px;padding:4px;border-bottom:1px solid #e2e2e2;height:32px}
  .avatar{width:19px;height:19px;background:#e9e9e9;border:1px solid #d0d0d0}
  .social-name{color:var(--blue-dark);font-weight:700;font-size:7px}
  .like{display:inline-block;border:1px solid #c0c0c0;background:#eee;font-size:5px;padding:0 2px;margin-top:2px}
  .fans{padding:4px;font-size:5.5px;border-bottom:1px solid #eee}
  .fans b{color:var(--blue-dark)}
  .faces{display:grid;grid-template-columns:repeat(3,24px);gap:3px 6px;padding:4px 6px}
  .face{text-align:center;font-size:5px;color:#666}
  .face span{display:block;width:24px;height:24px;background:#e6e6e6;border:1px solid #d2d2d2;margin-bottom:1px}
  .social-foot{position:absolute;left:0;bottom:0;width:100%;border-top:1px solid #e2e2e2;padding:2px 4px;font-size:5.5px;display:flex;align-items:center;gap:3px}
  .social-foot i{display:inline-block;width:6px;height:6px;background:var(--blue-dark)}

  /* Footer */
  .site-footer{position:absolute;left:0;top:1172px;width:680px;height:28px;background:var(--footer);border-top:2px solid var(--red);color:#fff;font-size:7.5px;text-align:center;line-height:26px}
</style>
</head>
<body>

<header class="site-header">
  <a class="brand" href="http://www.tourdepays.com/">tourdepays.com</a>
  <nav class="main-nav">
    <a href="#">Maison</a><span>|</span>
    <a href="#">Les régions</a><span>|</span>
    <a href="#">Grandes villes</a><span>|</span>
    <a href="#">Contactez</a>
  </nav>
  <div class="search">
    <svg width="11" height="11" viewBox="0 0 11 11" aria-hidden="true"><circle cx="4.5" cy="4.5" r="3.2" fill="none" stroke="#9a9a9a" stroke-width="1.3"/><line x1="6.8" y1="6.8" x2="10" y2="10" stroke="#9a9a9a" stroke-width="1.6"/></svg>
  </div>
</header>

<section class="hero" role="img" aria-label="Photo de village au bord d'une rivière sous une falaise boisée">
  <svg class="hero-arrow prev" width="22" height="44" viewBox="0 0 22 44" aria-hidden="true"><polyline points="21,1 1,22 21,43" fill="none" stroke="#fff" stroke-width="1.2"/></svg>
  <svg class="hero-arrow next" width="22" height="44" viewBox="0 0 22 44" aria-hidden="true"><polyline points="1,1 21,22 1,43" fill="none" stroke="#fff" stroke-width="1.2"/></svg>
  <div class="caption primary">Lorem ipsum dolor sit amet</div>
  <div class="caption secondary">Consectetur adipiscing elit</div>
</section>

<aside class="col col-left">
  <h3 class="widget-title">Les régions</h3>
  <ul class="link-list">
    <li>Alsace</li><li>Aquitaine</li><li>Auvergne</li><li>Basse-Normandie</li><li>Bourgogne</li><li>Bretagne</li><li>Centre</li><li>Champagne-Ardenne</li><li>Corse</li><li>Franche-Comté</li><li>Haute-Normandie</li><li>Île-de-France</li><li>Languedoc-Roussillon</li><li>Limousin</li><li>Lorraine</li><li>Midi-Pyrénées</li><li>Nord-Pas-de-Calais</li><li>Pays de la Loire</li><li>Picardie</li><li>Poitou-Charentes</li><li>Provence-Alpes-Côte d'Azur</li><li>Rhône-Alpes</li>
  </ul>
  <h3 class="widget-title" style="margin-top:15px">La France</h3>
  <ul class="link-list"><li>Statistique</li></ul>
</aside>

<div class="social">
  <div class="social-head">
    <span class="avatar"></span>
    <div><div class="social-name">tourdepays.com</div><div style="color:var(--blue-dark)">on Friendbook</div><span class="like">Like</span></div>
  </div>
  <div class="fans">5,000 people like <b>tourdepays.com</b></div>
  <div class="faces">
    <div class="face"><span></span>Léa</div>
    <div class="face"><span></span>Hugo</div>
    <div class="face"><span></span>Apples</div>
    <div class="face"><span></span>Marc</div>
    <div class="face"><span></span>Paul</div>
    <div class="face"><span></span>Bill</div>
  </div>
  <div class="social-foot"><i></i>Friendbook social plugin</div>
</div>

<main class="col col-main">
  <h1 class="section-title">Les villes de France</h1>
  <p class="lead">Trouvez ici les régions, départements et villes français.</p>
  <div class="map" role="img" aria-label="Carte de France colorée avec les frontières des régions"></div>

  <div class="copy" style="position:absolute;top:285px;left:0;width:251px">
    <p>Vous vous trouvez sur un site web dédié à vous donner toutes les informations dont vous avez besoin: Nous vous mettons à disposition une liste complète indiquant toutes les villes et tous les villages de France avec leurs codes postaux et des informations touristiques. Vous pouvez aussi télécharger les plus jolies photos de votre ville.</p>
    <p>&nbsp;En plus, vous trouvez ici des annonces immobilières qui vous aident à trouver la maison de vos rêves, des locaux appropriés pour votre nouveau bureau ou un petit appartement au centre-ville.</p>
    <p>Plusieurs informations supplémentaires, comme le service de météo, la possibilité d'inscrire votre propre siteweb lié à votre ville et les actualités locaux, rendent complet le total de notre offerte gratuite.</p>
  </div>
  <hr class="divider" style="position:absolute;top:419px;width:251px">

  <h2 class="section-title" style="position:absolute;top:430px">Les plus belles villes du mois</h2>
  <div class="copy" style="position:absolute;top:448px;left:0;width:251px">
    <p>La « capitale européenne » <span class="city">Strasbourg</span> est aussi la capitale historique de l'Alsace à l'est de la France. Strasbourg compte 272 500 habitants et est aussi le chef-lieu du département Bas-Rhin. Au fil du développement de l'union européenne, Strasbourg, aussi à cause de sa situation géographique à la frontière franco-allemande, est devenue siège d'un grand nombre d'institutions européennes, entre autres : Le Conseil de l'Europe, le Parlement européen et la Cour Européenne des droits de l'homme.</p>
    <div style="margin-top:9px">
      <div class="thumb"><span class="sea" role="img" aria-label="Vue de Marseille et de la mer"></span></div>
      <span class="city">Marseille</span> n'est pas seulement la ville la plus âgée de la France - à cause de son important port commercial, elle est aussi appelée « la porte au monde ». Fondée en 600 avant J.-C. par des marins Grecs de Phocée, Marseille est le premier port de la France. Marseille est le siège d'un archevêque, ville d'université et capitale de départements Bouches-du-Rhône. La ville doit son expansion et prospérité à son port, qui est un lieu de transbordement important pour des marchandises destinées pour l'Afrique du Nord et l'Asie. Spécialement le pétrole occupe une position éminente…
    </div>
  </div>
  <hr class="divider" style="position:absolute;top:643px;width:251px">

  <h2 class="section-title" style="position:absolute;top:655px">Actualités locales</h2>

  <article style="position:absolute;top:680px;width:251px">
    <h3 class="news-title">Russie: une Riot Chorus en grève de la faim pour protester contre le tribunal</h3>
    <div class="copy" style="margin-top:6px">
      <div class="thumb news"><span class="portrait" role="img" aria-label="Photo d'une jeune femme"></span></div>
      Une jeune femme du groupe contestataire russe Riot Chorus emprisonnée a entamé mercredi une grève de la faim après avoir été empêchée par la justice d'assister à l'audience sur sa demande de libération anticipée.
    </div>
    <a class="more" href="#" style="margin-top:2px">Savoir plus…</a>
  </article>
  <hr class="divider" style="position:absolute;top:772px;width:251px">

  <article style="position:absolute;top:784px;width:251px">
    <h3 class="news-title">Russie: une Riot Chorus en grève de la faim pour protester contre le tribunal</h3>
    <div class="copy" style="margin-top:6px">
      <div class="thumb news"><span class="portrait" role="img" aria-label="Photo d'une jeune femme"></span></div>
      Une jeune femme du groupe contestataire russe Riot Chorus emprisonnée a entamé mercredi une grève de la faim après avoir été empêchée par la justice d'assister à l'audience sur sa demande de libération anticipée.
    </div>
    <a class="more" href="#" style="margin-top:2px">Savoir plus…</a>
  </article>
  <hr class="divider" style="position:absolute;top:875px;width:251px">
</main>

<aside class="col col-right">
  <h3 class="widget-title">Les plus grandes villes</h3>
  <ul class="link-list">
    <li>Paris</li><li>Marseille</li><li>Lyon</li><li>Toulouse</li><li>Nice</li><li>Nantes</li><li>Strasbourg</li><li>Montpellier</li><li>Bordeaux</li><li>Lille</li><li>Rennes</li><li>Le Havre</li><li>Reims</li><li>Saint-Étienne</li><li>Toulon</li><li>Grenoble</li><li>Angers</li><li>Dijon</li><li>Brest</li><li>Le Mans</li><li>Clermont-Ferrand</li><li>Amiens</li><li>Aix-en-Provence</li><li>Limoges</li><li>Nîmes</li>
  </ul>
  <div class="ad" style="position:absolute;top:434px">250 x 250</div>
  <div class="ad promo" style="position:absolute;top:583px" role="img" aria-label="Bannière publicitaire illustrée pour un travail à domicile"></div>
  <div class="ad" style="position:absolute;top:731px">250 x 250</div>
</aside>

<footer class="site-footer">Copyright © 2013 tourdepays.com. All Rights Reserved.</footer>

</body>
</html>
```